Design some Business Cards

I NEED A BUSINESS CARD DESIGN AND A [login to view URL] IS MY OLD LOGO BUT USE YOUR CREATIVITY TO CREATE A DIFFERENT ONE (PICTURES ATTACHED).DESIGN A NEW LOGO AND BUSINESS CARD.
CHANGE EMAIL to dorin@velmqarte.com
add address: Brenmoor,Ontario
phone and and fax remain the same.

```html
<!DOCTYPE html>
<html lang="en">
<head>
<meta charset="utf-8">
<title>Marlo Vestwick – Business Cards</title>
<link rel="stylesheet" href="https://fonts.googleapis.com/css2?family=Montserrat:wght@500;600;700&display=swap">
<style>
  :root {
    --backdrop: #3a3a3c;
    --card-dark: #1e2023;
    --card-mid: #2b2e32;
    --card-fold: #33373c;
    --brand-red: #e0262b;
    --brand-green: #5fbf3a;
    --ink-light: #f2f2f2;
    --icon-bg: #f2f2f2;
    --icon-ink: #1e2023;
  }
  * { box-sizing: border-box; margin: 0; padding: 0; }
  html, body {
    width: 1200px; height: 900px; overflow: hidden;
    background: var(--backdrop);
    font-family: "Montserrat", sans-serif;
  }
  .sheet {
    position: relative; width: 1200px; height: 900px;
    display: flex; flex-direction: column; align-items: center; justify-content: center; gap: 34px;
  }
  .card {
    position: relative; width: 700px; height: 400px;
    background: var(--card-dark); overflow: hidden;
    box-shadow: 0 10px 30px rgba(0,0,0,.45);
  }
  .brand {
    position: absolute; display: flex; align-items: center; gap: 18px;
    white-space: nowrap;
  }
  .brand__square { background: var(--brand-green); flex: none; }
  .brand__name {
    color: var(--brand-red); font-weight: 700; letter-spacing: 1px; line-height: 1;
    text-transform: uppercase; white-space: nowrap;
  }
  .card--front .brand { left: 50%; top: 50%; transform: translate(-50%, -50%); }
  .card--front .brand__square { width: 44px; height: 44px; }
  .card--front .brand__name { font-size: 46px; }

  .card__panels { position: absolute; inset: 0; }
  .card--back .brand { left: 40px; top: 175px; gap: 12px; }
  .card--back .brand__square { width: 26px; height: 26px; }
  .card--back .brand__name { font-size: 25px; }

  .contact {
    position: absolute; right: 30px; top: 62px; width: 330px;
    color: var(--ink-light); text-align: right;
  }
  .contact__name {
    font-size: 21px; font-weight: 600; letter-spacing: .5px;
    margin: 0 36px 44px 0; text-transform: uppercase; white-space: nowrap;
  }
  .contact__list { list-style: none; display: flex; flex-direction: column; gap: 12px; }
  .contact__item {
    display: flex; align-items: center; justify-content: flex-end; gap: 12px;
    font-size: 14px; font-weight: 500; white-space: nowrap;
  }
  .contact__spacer { width: 30px; flex: none; }
  .contact__icon {
    width: 30px; height: 30px; border-radius: 50%;
    background: var(--icon-bg); display: flex; align-items: center; justify-content: center; flex: none;
  }
  .contact__icon--pin { background: var(--brand-red); }
  .contact__icon svg { width: 16px; height: 16px; }
</style>
</head>
<body>
<main class="sheet">

  <section class="card card--front" aria-label="Business card front">
    <div class="brand">
      <span class="brand__square"></span>
      <span class="brand__name">Marlo Vestwick</span>
    </div>
  </section>

  <section class="card card--back" aria-label="Business card back">
    <svg class="card__panels" viewBox="0 0 700 400" preserveAspectRatio="none" aria-hidden="true">
      <rect width="700" height="400" fill="var(--card-mid)"/>
      <polygon points="420,0 700,0 700,400 560,400 460,200" fill="var(--card-fold)"/>
      <polygon points="440,0 700,0 700,400 600,400 490,190" fill="var(--card-dark)"/>
    </svg>

    <div class="brand">
      <span class="brand__square"></span>
      <span class="brand__name">Marlo Vestwick</span>
    </div>

    <div class="contact">
      <p class="contact__name">Marlo Vestwick</p>
      <ul class="contact__list">
        <li class="contact__item"><span>+00145550127</span>
          <span class="contact__icon"><svg viewBox="0 0 24 24"><path fill="var(--icon-ink)" d="M6.6 10.8a15.1 15.1 0 0 0 6.6 6.6l2.2-2.2a1 1 0 0 1 1-.25 11.4 11.4 0 0 0 3.6.57 1 1 0 0 1 1 1V20a1 1 0 0 1-1 1A17 17 0 0 1 3 4a1 1 0 0 1 1-1h3.5a1 1 0 0 1 1 1c0 1.25.2 2.45.57 3.57a1 1 0 0 1-.25 1z"/></svg></span></li>
        <li class="contact__item"><span>104555019832</span>
          <span class="contact__icon"><svg viewBox="0 0 24 24"><path fill="var(--icon-ink)" d="M6 3h12v5H6zM4 9h16a2 2 0 0 1 2 2v6h-4v4H6v-4H2v-6a2 2 0 0 1 2-2zm4 6v4h8v-4z"/></svg></span></li>
        <li class="contact__item"><span>vestwickhomes.com</span>
          <span class="contact__icon"><svg viewBox="0 0 24 24"><circle cx="12" cy="12" r="9" fill="none" stroke="var(--icon-ink)" stroke-width="2"/><path d="M3 12h18M12 3c3 3 3 15 0 18M12 3c-3 3-3 15 0 18" fill="none" stroke="var(--icon-ink)" stroke-width="1.6"/></svg></span></li>
        <li class="contact__item"><span>dorin@velmqarte.com</span><span class="contact__spacer"></span></li>
        <li class="contact__item"><span>Brenmoor,Ontario</span>
          <span class="contact__icon contact__icon--pin"><svg viewBox="0 0 24 24"><path fill="#fff" d="M12 2a7 7 0 0 0-7 7c0 5 7 13 7 13s7-8 7-13a7 7 0 0 0-7-7zm0 9.5A2.5 2.5 0 1 1 12 6.5a2.5 2.5 0 0 1 0 5z"/></svg></span></li>
      </ul>
    </div>
  </section>

</main>
</body>
</html>
```